Stationery Design Project

KT7 Staffing requires letterhead and business card designs for a company based in London. Just like the name, we're a management resourcing company, providing resources to third party companies. You can see www.kt7staffing-example.com for ideas on existing colour schemes and design concepts that have been implimented and agreed to. Ultimately the design should broadcast professionalism, safety and the concept of growth.

Target Market(s)

Financial institutes; friendly societies (All UK based)

Industry/Entity Type

Safety

Requirements
Must have
• Files produced should be print ready; and the text in them editable (eg address, name etc)

```html
<!DOCTYPE html>
<html lang="en">
<head>
<meta charset="utf-8">
<title>KT7 Staffing — Stationery</title>
<link href="https://fonts.googleapis.com/css2?family=Didact+Gothic&display=swap" rel="stylesheet">
<style>
  :root {
    --paper-bg: #f2f3f3;
    --charcoal: #3d4343;
    --charcoal-light: #566060;
    --slate: #5e6767;
    --teal: #1d8c8c;
    --sky: #7cc1dc;
    --white: #ffffff;
    --ink: #4a4f4f;
    --muted: #8a9090;
  }
  * { box-sizing: border-box; margin: 0; padding: 0; }
  html, body { width: 1200px; height: 1175px; overflow: hidden; }
  body {
    position: relative;
    background: var(--paper-bg);
    font-family: "Didact Gothic", "Century Gothic", sans-serif;
    color: var(--ink);
  }

  /* ---------- shared brand header ---------- */
  .brand-header {
    position: absolute; left: 0; top: 0; width: 100%; height: 84px;
    background: var(--slate);
  }
  .brand-mark {
    position: absolute; left: 20px; top: 34px; width: 14px; height: 14px;
    background: var(--teal);
  }
  .brand-name {
    position: absolute; left: 44px; top: 25px;
    font-size: 26px; line-height: 32px; color: var(--teal);
    white-space: nowrap;
  }
  .bar-teal {
    position: absolute; left: 210px; right: 10px; top: 18px; height: 12px;
    background: var(--teal);
  }
  .bar-sky {
    position: absolute; left: 200px; right: 10px; top: 36px; height: 32px;
    background: var(--sky);
  }

  /* ---------- letterheads ---------- */
  .letterhead {
    position: absolute; top: 60px; width: 500px; height: 680px;
    box-shadow: 0 6px 18px rgba(0,0,0,.18);
    overflow: hidden;
  }
  .letterhead--reverse {
    left: 60px;
    background: radial-gradient(ellipse at 45% 40%, var(--charcoal-light) 0%, var(--charcoal) 70%);
  }
  .letterhead--front { left: 640px; background: var(--white); }

  .letterhead-footer {
    position: absolute; left: 0; bottom: 0; width: 100%; height: 86px;
    background: var(--slate);
  }
  .footer-name-block {
    position: absolute; left: 0; top: 14px; width: 240px; height: 56px;
    background: var(--sky); padding: 8px 14px;
  }
  .footer-name-block .person-name { font-size: 20px; color: var(--charcoal); }
  .footer-name-block .company { font-size: 12px; color: var(--charcoal); text-align: right; }
  .footer-divider {
    position: absolute; left: 248px; top: 14px; width: 16px; height: 56px;
    background: var(--sky);
  }
  .footer-contacts {
    position: absolute; left: 276px; top: 14px;
    font-size: 12.5px; color: #d6dcdc; line-height: 19px;
  }
  .contact-line { display: flex; align-items: center; gap: 6px; white-space: nowrap; }
  .contact-icon { width: 11px; height: 11px; flex: none; }

  .letter-body {
    position: absolute; left: 48px; top: 120px; right: 48px;
    font-size: 9.5px; line-height: 14px; color: #6b6262;
  }
  .recipient { margin-left: 260px; margin-bottom: 36px; }
  .letter-body p { margin-bottom: 14px; }

  .web-band {
    position: absolute; left: 36px; right: 0; bottom: 40px; height: 40px;
    background: var(--slate);
    color: #d8e0e0; font-size: 15px; letter-spacing: 2px;
    display: flex; align-items: center; justify-content: center;
  }

  /* ---------- business cards ---------- */
  .card {
    position: absolute; top: 820px; width: 400px; height: 230px;
    box-shadow: 0 6px 16px rgba(0,0,0,.2);
    overflow: hidden;
  }
  .card--reverse {
    left: 170px;
    background: radial-gradient(ellipse at 50% 50%, var(--charcoal-light) 0%, var(--charcoal) 75%);
  }
  .card--reverse .card-brand {
    position: absolute; left: 96px; top: 96px; display: flex; align-items: center; gap: 12px;
  }
  .card--reverse .brand-mark { position: static; width: 16px; height: 16px; }
  .card--reverse .brand-name { position: static; font-size: 32px; }

  .card--front { left: 630px; background: var(--white); }
  .card--front .brand-header { height: 70px; background: var(--white); }
  .card--front .brand-mark { top: 30px; }
  .card--front .brand-name { top: 22px; font-size: 24px; }
  .card--front .bar-teal { left: 190px; top: 14px; height: 10px; right: 0; }
  .card--front .bar-sky { left: 180px; top: 30px; height: 28px; right: 0; }
  .card-name { position: absolute; left: 22px; top: 96px; }
  .card-name .person-name { font-size: 16px; color: var(--teal); }
  .card-name .company { font-size: 10px; color: var(--ink); margin-left: 8px; }
  .card-contacts {
    position: absolute; top: 146px; font-size: 9.5px; line-height: 14px; color: var(--ink);
  }
  .card-contacts--left { left: 22px; }
  .card-contacts--right { left: 210px; }
  .card-contacts .contact-icon { width: 9px; height: 9px; }
  .social-dot { width: 9px; height: 9px; border-radius: 50%; background: var(--teal); flex: none; }
  .card-footer {
    position: absolute; left: 0; bottom: 0; width: 100%; height: 14px;
    background: var(--slate);
  }
</style>
</head>
<body>

<svg width="0" height="0" style="position:absolute">
  <defs>
    <symbol id="icon-pin" viewBox="0 0 12 12">
      <circle cx="6" cy="6" r="5.5" fill="#1d8c8c"/>
      <path d="M6 2.5a2.2 2.2 0 0 1 2.2 2.2C8.2 6.4 6 9 6 9S3.8 6.4 3.8 4.7A2.2 2.2 0 0 1 6 2.5z" fill="#fff"/>
    </symbol>
    <symbol id="icon-phone" viewBox="0 0 12 12">
      <circle cx="6" cy="6" r="5.5" fill="#1d8c8c"/>
      <path d="M4 3l1.2 1.4-.6.8c.4.9 1.1 1.6 2 2l.8-.6L9 7.8 8.2 9C6 8.7 3.3 6 3 3.8z" fill="#fff"/>
    </symbol>
    <symbol id="icon-mail" viewBox="0 0 12 12">
      <circle cx="6" cy="6" r="5.5" fill="#1d8c8c"/>
      <rect x="3" y="4" width="6" height="4.2" fill="#fff"/>
      <path d="M3 4l3 2.4L9 4" stroke="#1d8c8c" stroke-width=".7" fill="none"/>
    </symbol>
  </defs>
</svg>

<!-- Letterhead reverse -->
<section class="letterhead letterhead--reverse">
  <header class="brand-header">
    <span class="brand-mark"></span>
    <span class="brand-name">KT7 Staffing</span>
    <span class="bar-teal"></span>
    <span class="bar-sky"></span>
  </header>
  <footer class="letterhead-footer">
    <div class="footer-name-block">
      <div class="person-name">First, Last Name</div>
      <div class="company">KT7 Staffing</div>
    </div>
    <span class="footer-divider"></span>
    <div class="footer-contacts">
      <div class="contact-line"><svg class="contact-icon"><use href="#icon-pin"/></svg>Address, Country Zipcode</div>
      <div class="contact-line"><svg class="contact-icon"><use href="#icon-phone"/></svg>123.456.7890</div>
      <div class="contact-line"><svg class="contact-icon"><use href="#icon-mail"/></svg>hello@kt7staffing-example.com</div>
    </div>
  </footer>
</section>

<!-- Letterhead front -->
<section class="letterhead letterhead--front">
  <header class="brand-header">
    <span class="brand-mark"></span>
    <span class="brand-name">KT7 Staffing</span>
    <span class="bar-teal"></span>
    <span class="bar-sky"></span>
  </header>
  <article class="letter-body">
    <div class="recipient">Client Name<br>Company Street Address<br>City, Postcode</div>
    <p>Dear Client,</p>
    <p>Thank you for your recent enquiry about our resourcing services. We are pleased to outline how our team can support your organisation with experienced management professionals.</p>
    <p>Each placement is matched carefully to your needs, with clear reporting and a named contact throughout the engagement.</p>
    <p>Our consultants follow strict safety and compliance standards, giving your business confidence as it continues to grow.</p>
    <p>Please contact us at any time to arrange a meeting. We look forward to working with you.</p>
  </article>
  <div class="web-band">www.kt7staffing-example.com</div>
</section>

<!-- Business card reverse -->
<section class="card card--reverse">
  <div class="card-brand">
    <span class="brand-mark"></span>
    <span class="brand-name">KT7 Staffing</span>
  </div>
</section>

<!-- Business card front -->
<section class="card card--front">
  <header class="brand-header">
    <span class="brand-mark"></span>
    <span class="brand-name">KT7 Staffing</span>
    <span class="bar-teal"></span>
    <span class="bar-sky"></span>
  </header>
  <div class="card-name">
    <div class="person-name">First, Last Name</div>
    <div class="company">KT7 Staffing</div>
  </div>
  <div class="card-contacts card-contacts--left">
    <div class="contact-line"><svg class="contact-icon"><use href="#icon-pin"/></svg>Address, Country Zipcode</div>
    <div class="contact-line"><svg class="contact-icon"><use href="#icon-phone"/></svg>123.456.7890</div>
    <div class="contact-line"><svg class="contact-icon"><use href="#icon-mail"/></svg>hello@kt7staffing-example.com</div>
  </div>
  <div class="card-contacts card-contacts--right">
    <div class="contact-line"><span class="social-dot"></span>social.example/kt7</div>
    <div class="contact-line"><span class="social-dot"></span>network.example/kt7</div>
    <div class="contact-line"><span class="social-dot"></span>www.kt7staffing-example.com</div>
  </div>
  <div class="card-footer"></div>
</section>

</body>
</html>
```